Brochure for a software solution

Dear all,
PLEASE DO NOT SUBMIT YOUR DESIGNS IF YOU WERE NOT INVITED.
This was meant to be setup as a job for one designer only.
Apologies for the confusion.
Thank you.
Dear all,
This was meant to be setup as a job or one designer only.
Thank you.
Software

```html
<!DOCTYPE html>
<html lang="en">
<head>
<meta charset="utf-8">
<title>Lumen Intelligence Dashboards</title>
<link href="https://fonts.googleapis.com/css2?family=PT+Sans+Narrow:wght@400;700&family=Source+Sans+3:wght@300;400;600&family=Arimo:wght@400;700&display=swap" rel="stylesheet">
<style>
:root{
  --orange:#f39323;
  --orange-deep:#f07d14;
  --yellow:#ffd21a;
  --yellow-light:#fff27a;
  --text:#6d6e71;
  --text-soft:#8a8b8e;
  --panel:#f0f0f1;
  --row:#fdf2e6;
  --rule:#e8b98a;
  --white:#fff;
}
*{margin:0;padding:0;box-sizing:border-box}
html,body{width:1200px;height:928px;overflow:hidden;background:var(--white)}
.page{position:relative;width:1200px;height:928px;font-family:"Source Sans 3",sans-serif;color:var(--text)}
.header{position:absolute;left:0;top:0;width:1200px;height:78px;
  background:linear-gradient(180deg,var(--yellow-light) 0%,var(--yellow) 55%,#ffc21a 100%)}
.header::after{content:"";position:absolute;left:0;right:0;bottom:0;height:5px;background:linear-gradient(90deg,#ffe04a,#ffb020)}
.brands{position:absolute;right:52px;top:22px;display:flex;gap:0}
.brand{display:flex;align-items:center;gap:6px;padding:0 18px;height:36px;border-left:1px solid rgba(255,255,255,.6);
  font-family:"PT Sans Narrow",sans-serif;font-weight:700;font-size:19px;color:#f07d14}
.brand:first-child{border-left:none}
.brand .dot{width:16px;height:16px;border-radius:50%;background:#f07d14}
.side{position:absolute;left:820px;top:97px;width:380px;height:718px;background:var(--panel)}
.footer{position:absolute;left:0;top:815px;width:1200px;height:113px;
  background:linear-gradient(180deg,#ffd84a 0%,#ffb21f 35%,#f7941d 100%)}
.footer::before{content:"";position:absolute;left:0;right:0;top:8px;height:26px;
  background:repeating-linear-gradient(90deg,rgba(255,255,255,.18) 0 60px,rgba(255,255,255,0) 60px 140px)}
.footer .mail{position:absolute;left:46px;top:50px;font-size:13px;color:#ffe28a}
.footer .tag{position:absolute;right:68px;top:49px;font-family:"PT Sans Narrow",sans-serif;font-weight:700;font-size:14px;color:var(--white)}
.footer .num{position:absolute;right:14px;top:49px;font-family:"PT Sans Narrow",sans-serif;font-weight:700;font-size:14px;color:var(--white);padding-left:16px;border-left:1px solid rgba(255,255,255,.8);height:30px}
h1,h2,h3{font-family:"PT Sans Narrow",sans-serif;font-weight:700;color:var(--orange)}
.title{position:absolute;left:63px;top:153px;font-size:24px;letter-spacing:.2px}
.title-rule{position:absolute;left:63px;top:188px;width:712px;height:1px;background:#ddd}
.lead{position:absolute;left:63px;top:198px;width:730px;font-size:19.5px;line-height:25px;font-weight:300;color:var(--text-soft)}
.body{position:absolute;left:63px;width:730px;font-size:15px;line-height:23px;font-weight:300;color:var(--text-soft)}
.pricing-title{position:absolute;left:63px;top:448px;font-size:24px;font-weight:700}
.pricing{position:absolute;left:63px;top:484px;width:712px;border-collapse:collapse;background:var(--row);font-size:13px;color:var(--text)}
.pricing td{height:28.5px;border-bottom:1px solid var(--white);padding:0 14px;vertical-align:middle}
.pricing td+td{border-left:1px solid #e6e0d8;text-align:center}
.pricing td:first-child{width:287px;text-transform:uppercase;font-weight:400}
.pricing td:nth-child(2){width:200px}
.note{position:absolute;left:66px;top:785px;font-size:11.5px;font-weight:600;color:var(--text-soft)}
.note sup{font-size:8px}
.sec{position:absolute;left:849px;width:300px}
.sec h3{font-size:19px;line-height:21px;padding-bottom:6px;border-bottom:1px solid var(--rule);width:301px}
.sec p{font-size:13px;line-height:19.7px;font-weight:300;color:var(--text-soft);margin-top:7px}
.chart-box{position:absolute;left:1040px;top:196px;width:107px;height:75px;border:1px solid #c9c9c9;border-radius:4px;background:var(--white)}
.report{position:absolute;left:1058px;top:352px;width:84px;font-family:Arimo,sans-serif}
.report .rt{font-size:13px;line-height:14px;color:#333}
.report table{border-collapse:collapse;width:84px;margin-top:3px;font-size:7px;color:#333}
.report th{text-align:left;font-weight:700;padding:1px 3px 3px}
.report td{padding:2px 3px;height:12.8px}
.report tr.alt td{background:#dcdcdc}
.gauge{position:absolute;left:1030px;top:630px}
.gauge-cap{position:absolute;left:1045px;top:736px;font-family:Arimo,sans-serif;font-size:10.5px;color:#222}
</style>
</head>
<body>
<div class="page">
  <header class="header">
    <div class="brands">
      <div class="brand"><span class="dot"></span>Lumen BI</div>
      <div class="brand"><span class="dot"></span>Lumen Search</div>
      <div class="brand"><span class="dot"></span>Lumen Analytics</div>
    </div>
  </header>

  <aside class="side"></aside>

  <h1 class="title">LUMEN INTELLIGENCE DASHBOARDS</h1>
  <div class="title-rule"></div>
  <p class="lead">Dashboards built using Lumen Intelligence are unsurpassed when it comes to the ease of visual­izing data, the level of customization and the timeliness of information. But the users love Lumen Intelligence also because the dashboards present the information in a rich and engaging user interface.</p>
  <p class="body" style="top:309px">Each of the components has been designed with end user in mind, making sure that the information is presented in an efficient and well-designed manner at the same time making sure the user interface does not get in the way of the information.</p>
  <p class="body" style="top:389px">There is a number of pre-defined charts and gauges. These can be further configured to match a company’s existing branding or reflect any other specific requirements.</p>

  <h2 class="pricing-title">Server Pricing</h2>
  <table class="pricing">
    <tr><td>Lumen Server</td><td>$25,000 - $100,000 1</td><td></td></tr>
    <tr><td>Lumen API 2</td><td>$5,000 - $25,000 1</td><td></td></tr>
    <tr><td>CAL (per named user)</td><td>COST</td><td>COST PER USER 3</td></tr>
    <tr><td>25</td><td>$25,000</td><td>$1,000</td></tr>
    <tr><td>50</td><td>$47,500</td><td>$950</td></tr>
    <tr><td>100</td><td>$85,500</td><td>$855</td></tr>
    <tr><td>250</td><td>$115,000</td><td>$460</td></tr>
    <tr><td>500</td><td>$135,000</td><td>$270</td></tr>
    <tr><td>1000</td><td>$165,000</td><td>$165</td></tr>
    <tr><td>2500</td><td>$200,000</td><td>$80</td></tr>
  </table>
  <p class="note">All prices are in USD unless otherwise stated. <sup>1</sup> Contact us for details. &nbsp; <sup>2</sup> Optional. &nbsp; <sup>3</sup> Calculated for information purposes only.</p>

  <section class="sec" style="top:160px">
    <h3>CHARTS</h3>
    <p style="width:160px">Lumen Intelligence can visualize information using a variety of charts. The presentation is fully configurable by the end users.</p>
  </section>
  <div class="chart-box">
    <svg width="107" height="75" viewBox="0 0 107 75">
      <text x="32" y="8" font-family="Arimo,sans-serif" font-size="4" fill="#555">Sales by region</text>
      <ellipse cx="48" cy="44" rx="32" ry="20" fill="#7a3b8c"/>
      <path d="M48 40 L48 20 A32 20 0 0 1 78 34 Z" fill="#2e8b57"/>
      <path d="M48 40 L78 34 A32 20 0 0 1 70 54 Z" fill="#a0522d"/>
      <path d="M48 40 L70 54 A32 20 0 0 1 40 60 Z" fill="#c71585"/>
      <path d="M48 40 L40 60 A32 20 0 0 1 17 44 Z" fill="#d4a017"/>
      <path d="M48 40 L17 44 A32 20 0 0 1 24 27 Z" fill="#3cb371"/>
      <path d="M48 40 L24 27 A32 20 0 0 1 48 20 Z" fill="#8fbc8f"/>
      <rect x="86" y="6" width="18" height="24" fill="#eee" stroke="#ccc" stroke-width=".5"/>
      <g fill="#b22">
        <rect x="88" y="8" width="3" height="2"/><rect x="88" y="12" width="3" height="2" fill="#2e8b57"/>
        <rect x="88" y="16" width="3" height="2" fill="#7a3b8c"/><rect x="88" y="20" width="3" height="2" fill="#d4a017"/>
        <rect x="88" y="24" width="3" height="2" fill="#c71585"/>
      </g>
    </svg>
  </div>

  <section class="sec" style="top:318px">
    <h3>REPORTS</h3>
    <p style="width:205px">Dashboards can include reports ranging from simple tabular reports to complex reports with user-controlled grouping. Data within reports is fully searchable as well.</p>
  </section>
  <div class="report">
    <div class="rt">Sales by<br>sales person</div>
    <table>
      <tr><th>SalesPerson</th><th>Total</th></tr>
      <tr><td>Peter Jones</td><td>3168227</td></tr>
      <tr class="alt"><td>Ted Barnet</td><td>2206297</td></tr>
      <tr><td>Allen Mayfield</td><td>2196484</td></tr>
      <tr class="alt"><td>Keiko Chord</td><td>2157221</td></tr>
      <tr><td>Donato Monty</td><td>1588840</td></tr>
      <tr class="alt"><td>Barry Smith</td><td>1321891</td></tr>
      <tr><td>Bob White</td><td>1115845</td></tr>
      <tr class="alt"><td>Doug Rapien</td><td>1101333</td></tr>
      <tr><td>Eric Goldman</td><td>1076764</td></tr>
      <tr class="alt"><td>Al Grant</td><td>1020606</td></tr>
    </table>
  </div>

  <section class="sec" style="top:565px">
    <h3>GAUGES AND KEY<br>PERFORMANCE INDICATORS</h3>
    <p style="width:185px">Custom Key Performance Indicators can be visualized using any of the varieties of gauges (circular, linear or numeric). KPIs can also be colour-coded based on the target and warning levels.</p>
  </section>
  <svg class="gauge" width="130" height="110" viewBox="0 0 130 110">
    <circle cx="62" cy="60" r="56" fill="#9fb6d6"/>
    <circle cx="62" cy="60" r="56" fill="none" stroke="#5f7fb5" stroke-width="2" stroke-dasharray="1 3"/>
    <circle cx="62" cy="60" r="47" fill="#f39a1e"/>
    <path d="M62 60 L20 40 A47 47 0 0 0 38 100 Z" fill="#e2302b"/>
    <path d="M62 60 L104 46 A47 47 0 0 1 90 98 Z" fill="#1e9a4f"/>
    <rect x="44" y="28" width="36" height="10" rx="2" fill="#c8c8d8"/>
    <text x="62" y="36" text-anchor="middle" font-family="Arimo,sans-serif" font-size="8" fill="#fff">014122</text>
    <line x1="62" y1="60" x2="66" y2="107" stroke="#ccc" stroke-width="3"/>
    <circle cx="62" cy="60" r="6" fill="#ddd" stroke="#999"/>
    <g font-family="Arimo,sans-serif" font-size="7" fill="#333">
      <text x="32" y="18" transform="rotate(-35 32 18)">6000</text>
      <text x="92" y="12" transform="rotate(40 92 12)">9000</text>
      <text x="6" y="54" transform="rotate(90 6 54)">3000</text>
      <text x="118" y="64" transform="rotate(-70 118 64)">12000</text>
      <text x="13" y="108">0</text>
      <text x="70" y="106">14122</text>
    </g>
  </svg>
  <div class="gauge-cap">Division Quota - Drugs</div>

  <footer class="footer">
    <span class="mail">sales@lumenbi.com</span>
    <span class="tag">Ipsum lorem is ips</span>
    <span class="num">03</span>
  </footer>
</div>
</body>
</html>
```